Flyer Template Design

I have attached 4 files. I would like a design template that could be used across these documents so that they have a common look and feel. The content of the documents is tested and should not be changed significantly. The images can be changed. I have also attache our logo for color compatibility.
Updates

Need extra days to review

Target Market(s)

Wealthy Christian donors

Font styles to use
Serif
Sans Serif

```html
<!DOCTYPE html>
<html lang="en">
<head>
<meta charset="utf-8">
<title>The Harvest Trust – God's Heart for the Nations</title>
<link href="https://fonts.googleapis.com/css2?family=Cinzel:wght@500;600&family=Tinos:ital,wght@0,400;0,700;1,400;1,700&family=Open+Sans:ital,wght@1,300;1,400&display=swap" rel="stylesheet">
<style>
  :root {
    --sky: #5ccdf3;
    --sky-soft: #a9e3f7;
    --paper: #ffffff;
    --forest: #1e4a2c;
    --ink: #333333;
    --cta-blue: #00aeef;
    --cta-green: #8cc55a;
    --rule-blue: #b8dcef;
    --rule-green: #b9dba0;
    --photo-bg: #f0f1f3;
    --photo-label: #9aa3a8;
  }
  * { box-sizing: border-box; margin: 0; padding: 0; }
  html, body { width: 848px; height: 1200px; overflow: hidden; background: var(--paper); }
  .flyer { position: relative; width: 848px; height: 1200px; background: var(--paper); font-family: "Tinos", "Times New Roman", serif; color: var(--ink); }
  .hero-band {
    position: absolute; left: 23px; top: 22px; width: 803px; height: 740px;
    border-radius: 16px 0 0 0;
    background: linear-gradient(to bottom, var(--sky) 0%, var(--sky-soft) 45%, var(--paper) 100%);
  }
  .brand-tab {
    position: absolute; left: 575px; top: 22px; width: 251px; height: 112px;
    background: var(--paper); border-radius: 0 0 0 16px;
    display: flex; align-items: center; gap: 12px; padding-left: 26px;
  }
  .brand-mark { width: 18px; height: 18px; background: var(--forest); flex: none; }
  .brand-name { font-family: "Tinos", serif; font-size: 22px; line-height: 23px; letter-spacing: 1px; color: var(--forest); text-transform: uppercase; }
  .section-title {
    position: absolute; left: 77px; font-family: "Cinzel", serif; font-weight: 600;
    font-size: 29px; color: var(--forest); letter-spacing: 0.2px; line-height: 1;
  }
  .scripture { position: absolute; left: 77px; width: 680px; font-size: 13.6px; line-height: 19px; }
  .scripture p { position: absolute; left: 0; width: 680px; }
  .scripture em { font-weight: 700; }
  .column-text { position: absolute; left: 77px; width: 390px; font-size: 13.6px; line-height: 19px; text-align: justify; }
  .column-text p + p { margin-top: 19px; }
  .photo {
    position: absolute; background: var(--photo-bg);
    display: flex; align-items: center; justify-content: center;
    font-family: "Tinos", serif; font-size: 38px; color: var(--photo-label);
  }
  .tagline { position: absolute; left: 77px; width: 763px; top: 940px; display: flex; align-items: center; gap: 12px; }
  .tagline .rule { flex: 1; height: 1px; }
  .tagline .rule.left { background: var(--rule-blue); }
  .tagline .rule.right { background: var(--rule-green); }
  .tagline span { font-family: "Open Sans", sans-serif; font-style: italic; font-weight: 300; font-size: 18.5px; color: var(--ink); }
  .appeal { position: absolute; left: 80px; width: 688px; top: 1015px; font-size: 13.6px; line-height: 19px; text-align: center; }
  .cta {
    position: absolute; left: 67px; width: 714px; height: 39px; border-radius: 12px;
    display: flex; align-items: center; justify-content: center;
    font-family: "Open Sans", sans-serif; font-style: italic; font-weight: 300; font-size: 23px; color: #1a2a33;
  }
  .cta.join { top: 1079px; background: var(--cta-blue); }
  .cta.contact { top: 1129px; background: var(--cta-green); }
</style>
</head>
<body>
<main class="flyer">
  <div class="hero-band"></div>
  <div class="brand-tab">
    <div class="brand-mark"></div>
    <div class="brand-name">The<br>Harvest<br>Trust</div>
  </div>

  <h1 class="section-title" style="top:157px;">God’s Heart for the Nations</h1>

  <div class="scripture" style="top:195px;">
    <p style="top:0;">From beginning to end, the Bible reveals God’s heart for “the nations.”</p>
    <p style="top:38px;">In <em><i>Genesis,</i></em> God promises Abraham, “through your offspring all nations on the earth will be blessed.”</p>
    <p style="top:75px;">The <em><i>Psalms</i></em> prophesy that “all the nations you have made will come and worship before you, Lord…”</p>
    <p style="top:112px;">In <em><i>Isaiah,</i></em> God promises the Messiah, “I will make you a light to the nations, that my salvation may reach to the ends of the earth.”</p>
    <p style="top:169px;"><em><i>Daniel</i></em> sees “one like a son of man” who “was given authority, glory and sovereign power; all nations and peoples of every language worshiped him.”</p>
  </div>

  <div class="column-text" style="top:425px;">
    <p>In <b><i>Matthew,</i></b> Jesus commands his apostles to “Go and make disciples of all nations.” And he links his return to the completion of that task, saying, “This gospel of the kingdom will be preached in the whole world as a testimony to all nations, and then the end will come.”</p>
    <p>In <b><i>Revelation,</i></b> John sees a “great multitude that no one could number, from every nation, from all tribes and peoples and languages, standing before the throne…” In the Bible, the word “nations” refers to people groups: groups of people who share a common ethnicity, culture, and language. Amazingly, there are more than 12,000 of these nations scattered around the world—and God has promised that every one of them will be included in His Kingdom.</p>
  </div>
  <div class="photo" style="left:484px; top:429px; width:298px; height:237px;" role="img" aria-label="Photo of people from an unreached people group">Photos</div>

  <h2 class="section-title" style="top:713px;">Finishing the Task</h2>
  <div class="column-text" style="top:750px;">
    <p>Today, there are still 500 nations who are not yet represented in God’s Kingdom. No one has ever proclaimed the gospel to these “unengaged” people groups, and there are no believers among them. For these groups, God’s promises have yet to be fulfilled. Most of these groups are small and located in remote, difficult places. But because we now know who and where they are, by God’s grace it is possible that we can engage every one of them with the gospel within the next 3 years.</p>
  </div>
  <div class="photo" style="left:484px; top:749px; width:296px; height:140px;" role="img" aria-label="Photo of missionaries sharing the gospel in a remote village">Photos</div>

  <div class="tagline">
    <div class="rule left"></div>
    <span>You can make that happen.</span>
    <div class="rule right"></div>
  </div>

  <p class="appeal">Partner with the Harvest Trust and finance the missionaries who are taking the gospel for the first time to those last remaining people groups. Your investment will “hasten the coming of the day of God” by accelerating the effort to make “disciples in every nation.” In 2018, our partners helped take the gospel to 231 people groups in 35 countries.</p>

  <div class="cta join">Join us as we invest to make disciples in “all nations” by 2022.</div>
  <div class="cta contact">To learn more, email Daniel Carter at dcarter@harvesttrust.org.</div>
</main>
</body>
</html>
```